Bold Modern Creative Wine Label Needed for a Chardonnay

We need a modern, eye catching label, one that will appeal to millennials, but also attract the older more conservative crowd. We like the boldness of black on white but are open to your suggestions. Since the bottle type is a light green 'burgundy style' bottle, you should take that into account. The name of the brand is Vo`. The attached label is example of what we like very much. It is eye catching and bold and modern. Keep in mind that the bottle will be light green in color so black and white might not work so well. Use your creativity please! The label can be any size but needs to fit on this shape bottle. See attached photos. thanks!!

(Please no grapes or wine glasses or wine bottles featured on the label!)
Updates

Hi Designers, I just wanted to let you know that we received many great designs and we are sorting through them this week. The website is making it a bit difficult to create a 'poll' so this is taking longer than we expected. Thanks for all the great submissions!

```html
<!DOCTYPE html>
<html lang="en">
<head>
<meta charset="utf-8">
<title>Vò White Wine Label</title>
<link rel="stylesheet" href="https://fonts.googleapis.com/css2?family=Cinzel:wght@400&family=Cormorant+Garamond:wght@500&display=swap">
<style>
  :root {
    --backdrop: #eceee4;
    --label: #ffffff;
    --ink-dark: #2a2a10;
    --olive: #6f6f17;
    --rule: #8a8a5a;
  }
  html, body {
    margin: 0;
    padding: 0;
    width: 1200px;
    height: 1200px;
    overflow: hidden;
    background: var(--backdrop);
  }
  .canvas {
    position: relative;
    width: 1200px;
    height: 1200px;
  }
  .label {
    position: absolute;
    left: 100px;
    top: 146px;
    width: 1000px;
    height: 908px;
    background: var(--label);
    box-shadow: 0 2px 10px rgba(0,0,0,0.08);
  }
  .label-art {
    display: block;
    width: 1000px;
    height: 908px;
  }
  .vintage {
    font-family: "Cormorant Garamond", serif;
    font-weight: 500;
    font-size: 54px;
    font-variant-numeric: lining-nums;
    fill: var(--olive);
  }
  .brand-name {
    font-family: "Cormorant Garamond", serif;
    font-weight: 500;
    font-size: 330px;
    fill: var(--ink-dark);
  }
  .wine-type {
    font-family: "Cinzel", serif;
    font-weight: 400;
    font-size: 68px;
    letter-spacing: 2px;
    fill: var(--olive);
  }
  .divider {
    stroke: var(--rule);
    stroke-width: 3;
  }
  .volume {
    font-family: "Cormorant Garamond", serif;
    font-weight: 500;
    font-size: 38px;
    font-variant-numeric: lining-nums;
    fill: var(--ink-dark);
  }
</style>
</head>
<body>
  <div class="canvas">
    <div class="label">
      <svg class="label-art" viewBox="0 0 1000 908" xmlns="http://www.w3.org/2000/svg">
        <text class="vintage" x="16" y="468">2019</text>
        <text class="brand-name" x="460" y="540" text-anchor="middle">Vò</text>
        <text class="wine-type" x="495" y="748" text-anchor="middle">White Wine</text>
        <line class="divider" x1="266" y1="781" x2="724" y2="781"/>
        <text class="volume" x="495" y="855" text-anchor="middle">750ML 11.3% ALC/VOL</text>
      </svg>
    </div>
  </div>
</body>
</html>
```